Garlic Farm for Farm Sales/Restaurant sales

Need a professional, but appealing to agriculture world. We are selling 27 kinds of Organic Garlic from a farm in Simla,CO. I have uploaded logo and business information-we are going to need a template, because I will need to use it for four separate people.
-We are trying to appeal to Farm to table restaurants
-As well as growers/farmers

Target Market(s)

Agriculture Sales/Restaurants-Organic

Industry/Entity Type

Agriculture

Contact Information for Business Card

Want it to look more unique then your average orbel mart card- I want it to look amazing

Font styles to use
Sans Serif

Colors
0455a3
ec1f27
fbed22
ffffff

Requirements
Must have
• Just be creative
Nice to have
• Colorful
Should not have
• plain

```html
<!DOCTYPE html>
<html lang="en">
<head>
<meta charset="utf-8">
<title>Summit Ridge Gourmet Garlic – Business Card</title>
<link rel="stylesheet" href="https://fonts.googleapis.com/css2?family=Josefin+Sans:wght@400;600&display=swap">
<style>
  :root {
    --navy: #1a3060;
    --red: #ec1f27;
    --yellow: #fbdc0a;
    --white: #ffffff;
    --ink: #1d2f63;
    --backdrop: #2e2e30;
  }
  * { margin: 0; padding: 0; box-sizing: border-box; }
  html, body { width: 1200px; height: 900px; overflow: hidden; }
  body {
    background: var(--backdrop);
    font-family: "Josefin Sans", sans-serif;
    position: relative;
  }
  .card {
    position: absolute;
    width: 640px;
    height: 366px;
    overflow: hidden;
    box-shadow: 0 10px 24px rgba(0,0,0,.45);
  }

  /* back side */
  .card-back { left: 180px; top: 60px; background: var(--navy); }
  .card-back .accent-bar {
    position: absolute; left: 0; top: 268px;
    width: 400px; height: 26px; background: var(--yellow);
  }
  .brand {
    position: absolute; right: 46px; top: 96px;
    display: flex; align-items: center; gap: 14px;
  }
  .brand-dot { width: 54px; height: 54px; border-radius: 50%; background: var(--red); flex: none; }
  .brand-name {
    color: var(--white); font-weight: 600; font-size: 30px; line-height: 1.05;
  }
  .brand-name small { display: block; font-size: 15px; letter-spacing: 2px; font-weight: 600; }
  .social-row {
    position: absolute; right: 46px; top: 212px;
    display: flex; gap: 22px;
  }
  .social-row span {
    width: 22px; height: 22px; border-radius: 50%; background: var(--white);
  }

  /* front side */
  .card-front { left: 380px; top: 480px; background: var(--white); }
  .sun {
    position: absolute; left: 330px; top: -90px;
    width: 420px; height: 420px; border-radius: 50%; background: var(--yellow);
  }
  .sun-ring {
    position: absolute; left: 318px; top: -100px;
    width: 440px; height: 440px; border-radius: 50%;
    border: 3px solid var(--red); border-right-color: transparent; border-top-color: transparent;
  }
  .sun-brand {
    position: absolute; left: 410px; top: 120px; width: 230px;
    color: var(--navy); font-weight: 600; font-size: 30px; line-height: 1.05;
  }
  .sun-brand small { display: block; font-size: 15px; letter-spacing: 2px; }
  .edge-mark { position: absolute; left: 0; top: 150px; width: 12px; height: 18px; background: var(--red); }
  .edge-bar { position: absolute; left: 0; top: 168px; width: 8px; height: 120px; background: var(--yellow); }
  .contact { position: absolute; left: 44px; top: 142px; color: var(--ink); }
  .person { font-size: 30px; font-weight: 600; letter-spacing: 1.5px; line-height: 1; }
  .person .surname { color: var(--red); }
  .address { font-size: 15px; margin: 10px 0 14px; }
  .contact-line { display: flex; align-items: center; gap: 12px; font-size: 16px; margin-bottom: 9px; }
  .contact-line svg { width: 16px; height: 16px; flex: none; }
  .contact-line .hl { color: var(--red); }
</style>
</head>
<body>
  <section class="card card-back" aria-label="Card back">
    <div class="brand">
      <span class="brand-dot"></span>
      <div class="brand-name">Summit Ridge<small>GOURMET GARLIC</small></div>
    </div>
    <div class="social-row" aria-label="Social links">
      <span></span><span></span><span></span><span></span>
    </div>
    <div class="accent-bar"></div>
  </section>

  <section class="card card-front" aria-label="Card front">
    <div class="sun"></div>
    <div class="sun-ring"></div>
    <div class="sun-brand">Summit Ridge<small>GOURMET GARLIC</small></div>
    <div class="edge-mark"></div>
    <div class="edge-bar"></div>
    <div class="contact">
      <h1 class="person">DANA <span class="surname">WHITLOW</span></h1>
      <p class="address">P.O. Box 48 Ridgeton, CO 80912</p>
      <p class="contact-line">
        <svg viewBox="0 0 16 16"><rect width="16" height="16" rx="2" fill="#ec1f27"/><path d="M5 4l2 0 1 2.5-1.2 1a6 6 0 0 0 2.7 2.7l1-1.2 2.5 1v2a1 1 0 0 1-1 1A8 8 0 0 1 4 5a1 1 0 0 1 1-1z" fill="#fff"/></svg>
        555-014-2736
      </p>
      <p class="contact-line">
        <svg viewBox="0 0 16 16"><rect width="16" height="16" rx="2" fill="#ec1f27"/><rect x="3.5" y="5" width="9" height="6.5" fill="none" stroke="#fff" stroke-width="1.2"/><path d="M3.5 5l4.5 3.5L12.5 5" fill="none" stroke="#fff" stroke-width="1.2"/></svg>
        Dana@SRGarlic.com
      </p>
      <p class="contact-line">
        <svg viewBox="0 0 16 16"><rect width="16" height="16" rx="2" fill="#ec1f27"/><circle cx="8" cy="8" r="4.5" fill="none" stroke="#fff" stroke-width="1.1"/><path d="M3.5 8h9M8 3.5c-2 2.5-2 6.5 0 9M8 3.5c2 2.5 2 6.5 0 9" fill="none" stroke="#fff" stroke-width="1"/></svg>
        www.<span class="hl">SR</span>Garlic.com
      </p>
    </div>
  </section>
</body>
</html>
```